Photographic Tutorial website

We are looking for a fresh design for a photographic tutorial / workshop website. The website will have the included functions:

* Home (needs to have a login section)
* About Us
* Info about each course / workshop.
* Subscribe to courses and pay online.
* Members Area
* Photo gallery
* Contact us

The website will be implemented with our own made cms. We do not need it to be coded. We have a team ready to do this for us. We only need the PSD layout.

We have attached a mockup design that the client and I have come up with and we need the design to be taken to the next level.

Client also likes:
http://www.lumavistacamera.example/

Requirements
Must have
• Must Stand out i.e black backgrounds
Should not have
• Alter the logo in anyway.

```html
<!DOCTYPE html>
<html lang="en">
<head>
<meta charset="utf-8">
<title>Your Lens Mate – Photographic Tuition</title>
<link href="https://fonts.googleapis.com/css2?family=Oswald:wght@500;600&family=Arimo:ital,wght@0,400;1,400&display=swap" rel="stylesheet">
<style>
:root{
  --page:#151515;
  --header:#1c1c1c;
  --band:#2b2b2b;
  --content:#1b1b1b;
  --footer:#222;
  --green:#63b33a;
  --green-text:#6cc03e;
  --white:#fff;
  --muted:#4e4e4e;
  --quote:#c9c9c9;
  --box:#262626;
}
*{margin:0;padding:0;box-sizing:border-box}
html,body{width:1200px;height:1152px;overflow:hidden;background:var(--page)}
body{position:relative;font-family:"Arimo",Arial,sans-serif}
.abs{position:absolute}
.site-header{left:0;top:0;width:1200px;height:98px;background:linear-gradient(#232323,#161616)}
.brand{left:18px;top:16px;display:flex;align-items:center;gap:10px}
.brand-mark{width:46px;height:46px;border-radius:50%;background:var(--green)}
.brand-name{font-family:"Oswald",sans-serif;font-weight:600;font-size:38px;color:var(--white);line-height:1}
.brand-tag{left:76px;top:58px;width:380px;font-family:"Oswald",sans-serif;font-weight:500;font-size:13px;letter-spacing:6px;color:var(--white);border-bottom:2px solid #c24bbd;text-align:center}
.main-nav{left:516px;top:46px;display:flex;gap:4px}
.main-nav a{display:block;height:51px;line-height:51px;padding:0 17px;background:#101010;color:var(--white);text-decoration:none;font-family:"Oswald",sans-serif;font-weight:500;font-size:17px}
.main-nav a.active{background:var(--green)}
.spectrum{left:0;top:96px;width:1200px;height:3px;background:linear-gradient(90deg,#e03a3a,#f0a020,#e6e23a,#4bbf3a,#2d8fe0,#8a3ad6,#e03a9a)}
.hero-wrap{left:0;top:99px;width:1200px;height:460px;background:#0d0d0d}
.hero{left:16px;top:100px;width:1151px;height:427px;background:radial-gradient(ellipse at 40% 70%,#6b4a1e,#2a1c0e 45%,#0b0b10 85%)}
.dots{left:1081px;top:535px;display:flex;gap:6px}
.dots span{width:12px;height:12px;border-radius:50%;background:#3a3a3a}
.dots span.on{background:#eee}
.strip{left:0;top:559px;width:1200px;height:207px;background:repeating-linear-gradient(45deg,#2e2e2e 0 2px,#272727 2px 4px)}
.card{top:575px;width:257px;height:173px;background:var(--green);padding:3px}
.card .shot{width:251px;height:136px}
.card h3{font-family:"Oswald",sans-serif;font-weight:500;font-size:17px;color:var(--white);text-align:center;line-height:31px}
.arrow{top:637px;width:50px;height:50px;border-radius:50%;background:var(--green)}
.content{left:0;top:766px;width:1200px;height:317px;background:var(--content)}
.checklist{left:58px;top:780px;width:690px}
.checklist h2{font-family:"Oswald",sans-serif;font-weight:600;font-size:25px;color:var(--green-text);margin-bottom:8px}
.checklist p{font-size:11.8px;line-height:18.4px;color:var(--muted);margin-bottom:18px}
.quote{left:788px;top:783px;width:380px;height:92px;background:#0d0d0d;padding:9px 14px;font-style:italic;font-size:15.5px;line-height:23px;color:var(--quote)}
.quote b{color:var(--green-text);font-family:"Oswald",sans-serif;font-style:normal;font-size:20px;line-height:1}
.quote-tail{left:802px;top:875px}
.quote-name{left:826px;top:875px;font-family:"Oswald",sans-serif;font-weight:500;font-size:18px;color:var(--green-text)}
.gallery{left:788px;top:918px;width:380px;height:141px;background:var(--box);padding:10px 13px;border-top:1px solid #3a3a3a}
.gallery h4{font-family:"Oswald",sans-serif;font-weight:500;font-size:20px;color:var(--white);margin-bottom:8px}
.thumbs{display:flex;gap:13px}
.thumbs div{width:78px;height:78px;border:3px solid #444;background:linear-gradient(#1a1010,#c8381a 45%,#e8b020 75%,#1a1208)}
.site-footer{left:0;top:1083px;width:1200px;height:57px;background:var(--footer)}
.copy{left:58px;top:1103px;font-size:11.5px;color:#aaa}
.social{top:1085px;width:48px;height:48px;border-radius:50%;border:2px solid #555;background:radial-gradient(#2a2a2a,#0e0e0e);display:flex;align-items:center;justify-content:center}
</style>
</head>
<body>
<header class="abs site-header"></header>
<div class="abs brand"><span class="brand-mark"></span><span class="brand-name">Your Lens Mate</span></div>
<div class="abs brand-tag">PHOTOGRAPHIC TUITION</div>
<nav class="abs main-nav">
  <a class="active" href="#">Home</a><a href="#">About Us</a><a href="#">Course</a><a href="#">Members Area</a><a href="#">Photo gallery</a><a href="#">Contact us</a>
</nav>
<div class="abs spectrum"></div>

<div class="abs hero-wrap"></div>
<div class="abs hero" role="img" aria-label="Night-time aerial photograph of a city street lined with lit buildings and palm trees"></div>
<div class="abs dots"><span class="on"></span><span></span><span></span><span></span><span></span></div>

<section class="abs strip"></section>
<div class="abs arrow" style="left:16px">
  <svg width="50" height="50" viewBox="0 0 50 50"><path d="M29 14 L19 25 L29 36" fill="none" stroke="#1b1b1b" stroke-width="5" stroke-linecap="round" stroke-linejoin="round"/></svg>
</div>
<div class="abs arrow" style="left:1118px">
  <svg width="50" height="50" viewBox="0 0 50 50"><path d="M21 14 L31 25 L21 36" fill="none" stroke="#1b1b1b" stroke-width="5" stroke-linecap="round" stroke-linejoin="round"/></svg>
</div>
<article class="abs card" style="left:58px"><div class="shot" role="img" aria-label="City skyline at dusk" style="background:linear-gradient(#2a3a70,#c06a7a 40%,#2a2a40 75%,#151520)"></div><h3>Top City</h3></article>
<article class="abs card" style="left:328px"><div class="shot" role="img" aria-label="Black and white photograph of a kitten" style="background:radial-gradient(ellipse at 50% 60%,#8a8478,#3a3630 55%,#151412)"></div><h3>Animal</h3></article>
<article class="abs card" style="left:598px"><div class="shot" role="img" aria-label="Bridge and skyline lit up at night" style="background:linear-gradient(#3a0808,#c83a14 45%,#1a1008 70%,#b8c020 90%,#1a1a08)"></div><h3>Night Photo</h3></article>
<article class="abs card" style="left:869px"><div class="shot" role="img" aria-label="Modern glass building at twilight" style="background:linear-gradient(160deg,#1a2a8a,#3a50c0 45%,#6a4030 70%,#1a1410)"></div><h3>City Walks</h3></article>

<main class="abs content"></main>
<section class="abs checklist">
  <h2>Photography check list</h2>
  <p>Lorem Ipsum is simply dummy text of the printing and typesetting industry. Lorem Ipsum has been the industry's standard dummy text ever since the 1500s, when an unknown printer took a galley of type and scrambled it to make a type specimen book. It has survived not only five centuries, but also the leap into electronic typesetting, remaining essentially unchanged. It was popularised in the 1960s with the release of Typeline sheets containing Lorem Ipsum passages, and more recently with desktop publishing software like Pagecraft Studio including versions of Lorem Ipsum.</p>
  <p>Lorem Ipsum is simply dummy text of the printing and typesetting industry. Lorem Ipsum has been the industry's standard dummy text ever since the 1500s, when an unknown printer took a galley of type and scrambled it to make a type specimen book. It has survived not only five centuries, but also the leap into electronic typesetting, remaining essentially unchanged. It was popularised in the 1960s with the release of Typeline sheets containing Lorem Ipsum passages, and more recently with desktop publishing software like Pagecraft Studio including versions of Lorem Ipsum.</p>
</section>
<blockquote class="abs quote"><b>“</b> Lorem Ipsum is simply dummy text of the printing and typesetting industry. Lorem Ipsum has been the industry's standard dummy text ever. <b>”</b></blockquote>
<svg class="abs quote-tail" width="20" height="16" viewBox="0 0 20 16"><path d="M0 0 H20 L18 16 Z" fill="#0d0d0d"/></svg>
<div class="abs quote-name">Dana Corwell</div>
<aside class="abs gallery">
  <h4>Members Gallery</h4>
  <div class="thumbs">
    <div role="img" aria-label="Member photo of a bridge at night"></div>
    <div role="img" aria-label="Member photo of a bridge at night"></div>
    <div role="img" aria-label="Member photo of a bridge at night"></div>
    <div role="img" aria-label="Member photo of a bridge at night"></div>
  </div>
</aside>

<footer class="abs site-footer"></footer>
<div class="abs copy">All images © 2011 Lumavista Photography Workshops.</div>
<a class="abs social" style="left:966px" href="#" aria-label="Social profile"></a>
<a class="abs social" style="left:1018px" href="#" aria-label="Email">
  <svg width="26" height="18" viewBox="0 0 26 18"><rect x="1" y="1" width="24" height="16" fill="none" stroke="#666" stroke-width="2"/><path d="M1 1 L13 10 L25 1" fill="none" stroke="#666" stroke-width="2"/></svg>
</a>
<a class="abs social" style="left:1070px" href="#" aria-label="Social profile"></a>
<a class="abs social" style="left:1122px" href="#" aria-label="News feed"></a>
</body>
</html>
```